Online-Marketing-Material für Reinigungsunternehmen
Zielgruppe
Wir sind ein seit Jahresanfang bestehende Reinigungsunternehmen.
Unsere Schwerpunkte liegen auf Treppenhausreinigung und Büroreinigung.
Die Anzeige soll auf Facebook / Instagram als Werbung angezeigt werden.
Kunden sind sowohl Unternehmer sowie auch Privathaushalte und Hausverwaltungen.
www.kolvaputz.de
Aufgabenstellung
Es darf gerne Modern und verspielt sein. Es soll und darf nicht billig wirken.
Wir haben auch ein Maskottchen. Es muss aber nicht auf die Anzeige mit drauf!

```html
<!DOCTYPE html>
<html lang="de">
<head>
<meta charset="utf-8">
<title>Kolva Putz – Anzeige</title>
<link rel="stylesheet" href="https://fonts.googleapis.com/css2?family=Poppins:wght@400;500;600;700;800&display=swap">
<style>
  :root {
    --wood-dark: #3e2719;
    --wood-mid: #6a452d;
    --wood-light: #8a5d3f;
    --tool-blue: #3d8fd6;
    --overlay-blue: rgba(72, 140, 214, 0.86);
    --band-blue: #2f4f9c;
    --button-text: #3a7fcf;
    --arrow-green: #6cbf2a;
    --white: #ffffff;
  }
  * { margin: 0; padding: 0; box-sizing: border-box; }
  html, body { width: 1200px; height: 1200px; overflow: hidden; background: var(--white); }
  .ad {
    position: relative;
    width: 1200px;
    height: 1200px;
    overflow: hidden;
    font-family: "Poppins", sans-serif;
    color: var(--white);
  }
  .cleaning-photo {
    position: absolute;
    left: 0; top: 0;
    width: 1200px; height: 994px;
    background:
      radial-gradient(ellipse 260px 320px at 1070px 230px, rgba(61,143,214,0.75), transparent 70%),
      radial-gradient(ellipse 200px 160px at 520px 440px, rgba(230,236,245,0.55), transparent 70%),
      radial-gradient(ellipse 180px 220px at 60px 660px, rgba(61,143,214,0.6), transparent 70%),
      linear-gradient(100deg, var(--wood-dark) 0%, var(--wood-mid) 35%, var(--wood-light) 55%, var(--wood-mid) 80%, var(--wood-dark) 100%);
  }
  .diagonal-overlay {
    position: absolute;
    left: 0; top: 0;
    width: 1200px; height: 994px;
  }
  .brand {
    position: absolute;
    left: 99px; top: 118px;
  }
  .brand-name {
    font-weight: 700;
    font-size: 66px;
    line-height: 1.02;
    color: var(--white);
  }
  .brand-owner {
    margin-top: 10px;
    font-weight: 400;
    font-size: 24px;
    color: var(--white);
  }
  .headline {
    position: absolute;
    left: 97px; top: 686px;
    font-weight: 700;
    text-transform: uppercase;
    line-height: 1;
  }
  .headline-small { font-size: 68px; letter-spacing: 0.5px; }
  .headline-large { font-size: 122px; margin-top: 8px; letter-spacing: -1px; font-weight: 800; }
  .services {
    position: absolute;
    top: 888px;
    left: 0;
    width: 1200px;
    font-weight: 500;
    font-size: 40px;
    line-height: 1;
  }
  .service {
    position: absolute;
    display: flex;
    align-items: center;
    gap: 16px;
    white-space: nowrap;
  }
  .service svg { width: 30px; height: 24px; }
  .service--offices { left: 99px; }
  .service--stairs { left: 305px; }
  .service--homes { left: 717px; }
  .info-band {
    position: absolute;
    left: 0; top: 994px;
    width: 1200px; height: 206px;
    background: var(--band-blue);
  }
  .tagline {
    position: absolute;
    left: 99px; top: 1050px;
    font-weight: 500;
    font-size: 28.5px;
    line-height: 48px;
  }
  .cta-button {
    position: absolute;
    left: 871px; top: 1063px;
    width: 230px; height: 72px;
    background: var(--white);
    border-radius: 10px;
    display: flex;
    align-items: center;
    justify-content: center;
    gap: 10px;
    color: var(--button-text);
    font-weight: 700;
    font-size: 31px;
    text-decoration: none;
  }
  .cta-button svg { width: 20px; height: 26px; }
</style>
</head>
<body>
<div class="ad">
  <div class="cleaning-photo" role="img" aria-label="Draufsicht auf blaue Reinigungsutensilien auf dunklem Holzboden: Farbroller, Kehrschaufel mit Handfeger, Schwamm, Gummihandschuhe und Sprühflasche"></div>

  <svg class="diagonal-overlay" viewBox="0 0 1200 994" aria-hidden="true">
    <polygon points="0,736 1200,497 1200,994 0,994" fill="var(--overlay-blue)"/>
  </svg>

  <div class="brand">
    <div class="brand-name">Kolva<br>Putz</div>
    <div class="brand-owner">Inh. Jonas Reberg</div>
  </div>

  <h1 class="headline">
    <div class="headline-small">Schenken Sie Ihrem Objekt</div>
    <div class="headline-large">Neuen Glanz</div>
  </h1>

  <div class="services">
    <div class="service service--offices">
      <svg viewBox="0 0 30 24"><polyline points="3,12 11,20 27,4" fill="none" stroke="var(--white)" stroke-width="4" stroke-linecap="round" stroke-linejoin="round"/></svg>
      Büros
    </div>
    <div class="service service--stairs">
      <svg viewBox="0 0 30 24"><polyline points="3,12 11,20 27,4" fill="none" stroke="var(--white)" stroke-width="4" stroke-linecap="round" stroke-linejoin="round"/></svg>
      Treppenhäuser
    </div>
    <div class="service service--homes">
      <svg viewBox="0 0 30 24"><polyline points="3,12 11,20 27,4" fill="none" stroke="var(--white)" stroke-width="4" stroke-linecap="round" stroke-linejoin="round"/></svg>
      Privathaushalte
    </div>
  </div>

  <div class="info-band"></div>

  <p class="tagline">Zuverlässige, professionelle Reinigungskräfte<br>in den Kreisen Paderborn &amp; Gütersloh</p>

  <a class="cta-button" href="#">
    Anfragen
    <svg viewBox="0 0 20 26"><polyline points="4,3 15,13 4,23" fill="none" stroke="var(--arrow-green)" stroke-width="6" stroke-linejoin="miter"/></svg>
  </a>
</div>
</body>
</html>
```